Crestfield Row sign

24"x36" sign for new home construction job site. Located in affluent in-town neighborhood in Midwest. Traditional american style homes. 2nd generation construction company. Sign needs to convey strength and elegance but not overly elaborate. Competition most has signs consisting of text.

Sign text reads:
Crestfield Row Builders
Custom Luxury for Over 20 years
248-391-0827

Target Market(s)

Upper middle income home buyers

Industry/Entity Type

Construction

Font styles to use
Serif
Decorative

Requirements
Must have
• Logo image no more than 2 colors
Nice to have
• Should be visible and legible from distance of 30'
Should not have
• Not just image of house as logo

```html
<!DOCTYPE html>
<html lang="en">
<head>
<meta charset="utf-8">
<title>Crestfield Row Builders – Job Site Sign</title>
<link rel="stylesheet" href="https://fonts.googleapis.com/css2?family=Sorts+Mill+Goudy&family=Libre+Caslon+Text:wght@700&display=swap">
<style>
  :root {
    --page-bg: #ffffff;
    --sign-black: #1b1a18;
    --sign-gold: #e8c882;
    --ink-gold: #e8c882;
    --ink-black: #1b1a18;
  }
  html, body {
    margin: 0;
    padding: 0;
    width: 1200px;
    height: 943px;
    overflow: hidden;
    background: var(--page-bg);
  }
  .sign-sheet {
    display: block;
    width: 1200px;
    height: 943px;
  }
  .company-name {
    font-family: "Sorts Mill Goudy", serif;
    letter-spacing: 0.01em;
  }
  .tagline {
    font-family: "Sorts Mill Goudy", serif;
  }
  .phone-number {
    font-family: "Libre Caslon Text", serif;
    font-weight: 700;
  }
  .sign--dark .sign-panel { fill: var(--sign-black); }
  .sign--dark .sign-text { fill: var(--ink-gold); }
  .sign--light .sign-panel { fill: var(--sign-gold); }
  .sign--light .sign-text { fill: var(--ink-black); }
</style>
</head>
<body>
<svg class="sign-sheet" viewBox="0 0 1200 943" xmlns="http://www.w3.org/2000/svg" role="img" aria-label="Two arrow-shaped signs for Crestfield Row Builders: a black version with gold lettering and a gold version with black lettering">

  <!-- Dark sign -->
  <g class="sign sign--dark">
    <path class="sign-panel" d="M292 116 H815 V171 L921 311 L815 440 V507 H292 Z"/>
    <text class="sign-text company-name" x="559" y="227" font-size="47" text-anchor="middle">CRESTFIELD ROW</text>
    <text class="sign-text company-name" x="559" y="283" font-size="47" text-anchor="middle">BUILDERS</text>
    <text class="sign-text tagline" x="559" y="356" font-size="30" text-anchor="middle">Custom Luxury for Over 20 Years..</text>
    <g class="sign-text phone" transform="translate(372 406)">
      <path class="phone-icon" d="M6 0 C2 2 0 6 1 12 C3 24 10 36 18 44 C21 46 24 46 26 44 L29 40 C30 38 29 36 27 35 L21 32 C19 31 17 32 16 34 L15 35 C11 30 8 23 7 17 L9 16 C11 15 12 13 11 11 L9 3 C8 1 7 0 6 0 Z"/>
      <text class="phone-number" x="44" y="38" font-size="44">248-391-0827</text>
    </g>
  </g>

  <!-- Light sign -->
  <g class="sign sign--light">
    <path class="sign-panel" d="M352 563 H735 V603 L813 707 L735 803 V849 H352 Z"/>
    <text class="sign-text company-name" x="548" y="649" font-size="36" text-anchor="middle">CRESTFIELD ROW</text>
    <text class="sign-text company-name" x="548" y="689" font-size="36" text-anchor="middle">BUILDERS</text>
    <text class="sign-text tagline" x="548" y="740" font-size="22" text-anchor="middle">Custom Luxury for Over 20 Years..</text>
    <g class="sign-text phone" transform="translate(434 770) scale(0.72)">
      <path class="phone-icon" d="M6 0 C2 2 0 6 1 12 C3 24 10 36 18 44 C21 46 24 46 26 44 L29 40 C30 38 29 36 27 35 L21 32 C19 31 17 32 16 34 L15 35 C11 30 8 23 7 17 L9 16 C11 15 12 13 11 11 L9 3 C8 1 7 0 6 0 Z"/>
      <text class="phone-number" x="44" y="37" font-size="43">248-391-0827</text>
    </g>
  </g>

</svg>
</body>
</html>
```